CupTradeHub

-
Below info still applicable but I wanted to highlight the point that I am looking for a design similar to the style linkloop+ with the mentioned color scheme (below). If you do that then the project is yours, I'm happy with an almost clone design. I know this is a completely different type of app but what I mean is:
- The listings to look like the linkloop+ widgets (i.e. blocks, three column, and clearly seperated)
- Adverts and listings mixed together in the results set
- Prominent listings to take up 2 or 3 of the columns instead, non prominent ones to take up 1.
- Clear spacing between the listings, as with linkloop+ widgets
- Clear seperation between menu and widgets as with linkloop+
- Search/filters and category filters on the right or left, as with linkloop+
Again, if this is not clear I want it LIKE LINKLOOP+, so far had stock template designs that weren't anything like this.
Linkloop+ is not the only site I listed for inspiration, but I think its easier at this point to just say clone the damn thing, and re purpose it for coffee. We will make additional changes at development time to make it distinct and incorporate some of the other things we were looking for.
-
Hi All,
I'm looking to get designs for a new site that allows coffee roasters, and barista equipment suppliers to sell their goods to coffee shops via an auction site. So essentially B2B bidnest targeted at the coffee market.
Pages required:
All pages:
- Logo
- Login/register links (or my account if logged in)
- links to Contact us, FAQs, Advertise with us
Homepage:
- Search bar
- List of filter categories
- Latest products section
- Advertising section
Search page:
- Listings (Image, price (buy now or current bid), postage price, no bids, time remaining to bid)
- Advertising
Listing page
- Same listing info as above but with full description, multipule images to select from, time ending and and a bid form (enter amount) or buy now button.
Login page
- Username/Password
- Alternative login via Friendora
My account:
- Link to add listings
- List of current listings
- List of current bids
- Link to purchase history
Add a listing:
- Form page to add a listing
- Requires
- Images uploads (drag to upload, as well as normal)
- Title field
- Description field
- Amount field
- Quantity field
- Postage amount field
- Category Drop down field
- End date/time picker field
That's it for functionality, with regards to design this needs to be designed in a way that is compatible with scaffoldr components (http://chirpnet.codehost.example/scaffoldr/), though scaffoldr is highly customizable so don't feel too restricted.
Styles/colours:
Site layout should be clean, and clear utilizing white space well i.e.
- http://shrt.example/qpWmT
- http://shrt.example/VbRdK
- https://circles.linkloop.example/
Also VERY much like the vantasoft "tiler" style design i.e. square boxes. If you know what I mean by this then cool, if not don't worry about it.
The logo on the other hand should have and earthy, organic feel to it.
Also, please only use fonts available from typevault fonts (http://www.typevault.example/fonts/).

```html
<!DOCTYPE html>
<html lang="en">
<head>
<meta charset="utf-8">
<title>CupTradeHub</title>
<link rel="stylesheet" href="https://fonts.googleapis.com/css2?family=Arimo:wght@400;700&family=Tinos&display=swap">
<style>
:root{
  --brown:#a8623d;
  --brown-title:#b06b43;
  --ink:#333333;
  --muted:#555555;
  --main-bg:#e6e6e6;
  --side-bg:#efefef;
  --card-bg:#f7f7f7;
  --line:#cfcfcf;
  --footer-bg:#d6d6d6;
  --ad-bg:#d9d9d9;
}
*{box-sizing:border-box;margin:0;padding:0}
html,body{width:1200px;height:778px;overflow:hidden}
body{position:relative;font-family:"Arimo",Arial,sans-serif;color:var(--ink);background:#fff}
.abs{position:absolute}

/* header */
.site-header{position:absolute;left:0;top:0;width:1200px;height:111px;background:linear-gradient(#ffffff,#f1f1f1)}
.site-header::after{content:"";position:absolute;left:0;right:0;top:106px;height:4px;background:var(--brown)}
.brand{position:absolute;left:14px;top:10px;display:flex;align-items:center;gap:12px}
.brand-dot{width:80px;height:80px;border-radius:50%;background:var(--brown)}
.brand-name{font-family:"Tinos",Georgia,serif;font-size:30px;color:var(--brown)}

.main-nav{position:absolute;top:71px;left:0;height:36px}
.tab{position:absolute;top:0;height:36px;background:#c9c9c9;clip-path:polygon(12px 0,100% 0,100% 100%,0 100%)}
.tab span{position:absolute;inset:1px 1px 0 1px;background:linear-gradient(#ffffff,#ececec);clip-path:polygon(12px 0,100% 0,100% 100%,0 100%);display:flex;align-items:center;justify-content:center;padding-left:6px;font-family:"Tinos",Georgia,serif;font-size:18px;color:#333}
.tab.active{background:var(--brown)}
.tab.active span{background:var(--brown);color:#fff}

/* main */
.main{position:absolute;left:0;top:110px;width:873px;height:608px;background:var(--main-bg)}
.section-title{position:absolute;left:20px;top:28px;font-size:21px;color:#333}
.pager-info{position:absolute;left:677px;top:33px;font-size:14px;color:#555}
.pager-btn{position:absolute;top:26px;width:28px;height:28px;background:#f8f8f8;border:1px solid #cfcfcf;border-radius:2px}
.pager-btn svg{display:block;margin:8px auto}

.card{position:absolute;width:408px;height:171px;background:var(--card-bg);border:1px solid var(--line);box-shadow:0 1px 2px rgba(0,0,0,.12)}
.card .photo{position:absolute;left:11px;top:11px;width:184px;height:145px}
.price{position:absolute;left:219px;top:14px;font-size:30px;color:#333}
.time-label{position:absolute;left:219px;top:66px;display:flex;align-items:center;gap:9px;font-size:17px;color:#333}
.timer{position:absolute;left:221px;top:107px;width:164px;height:38px;background:#fff;border:1px solid #d2d2d2;font-size:19px;display:flex;align-items:center;justify-content:center;color:#333}

/* footer */
.site-footer{position:absolute;left:0;top:718px;width:873px;height:60px;background:var(--footer-bg);font-size:14px;color:#555}
.site-footer .copy{position:absolute;left:10px;top:26px}
.site-footer .rights{position:absolute;right:5px;top:26px}

/* sidebar */
.sidebar{position:absolute;left:873px;top:110px;width:327px;height:668px;background:var(--side-bg);border-left:1px solid #d8d8d8}
.side-title{position:absolute;left:13px;top:31px;font-size:25px;color:var(--brown-title)}
.field{position:absolute;background:#fff;border:1px solid #cfcfcf;border-radius:3px;font-size:15px;color:#999;display:flex;align-items:center;padding-left:14px}
.select{position:absolute;background:linear-gradient(#f7f7f7,#e6e6e6);border:1px solid #cfcfcf;border-radius:3px;font-size:14px;color:#444;display:flex;align-items:center;padding-left:10px}
.select::after{content:"";position:absolute;right:10px;top:50%;margin-top:-3px;border-left:5px solid transparent;border-right:5px solid transparent;border-top:7px solid #555}
.range-label{position:absolute;left:14px;top:271px;font-size:13px;color:#444}
.ticks{position:absolute;left:13px;top:306px;width:296px;height:20px;font-size:11px;color:#555}
.ticks span{position:absolute;transform:translateX(-50%)}
.track{position:absolute;left:14px;top:333px;width:296px;height:10px;background:#d4d4d4;border-radius:2px}
.track i{position:absolute;left:4px;right:28px;top:3px;height:3px;background:var(--brown)}
.handle{position:absolute;top:350px}
.btn{position:absolute;top:401px;height:45px;border-radius:3px;font-size:16px;display:flex;align-items:center;justify-content:center}
.btn-primary{left:14px;width:153px;background:var(--brown);color:#fff}
.btn-light{left:173px;width:140px;background:linear-gradient(#fbfbfb,#e4e4e4);border:1px solid #cccccc;color:#555}
.ad-slot{position:absolute;left:7px;top:482px;width:313px;height:180px;background:var(--ad-bg);display:flex;flex-direction:column;align-items:center;justify-content:center;color:#555}
.ad-slot .size{font-size:27px}
.ad-slot .hint{font-size:17px}
</style>
</head>
<body>

<header class="site-header">
  <div class="brand">
    <div class="brand-dot"></div>
    <div class="brand-name">CupTradeHub</div>
  </div>
  <nav class="main-nav">
    <a class="tab active" style="left:374px;width:137px"><span>Home</span></a>
    <a class="tab" style="left:518px;width:186px"><span>Advertise with us</span></a>
    <a class="tab" style="left:711px;width:93px"><span>FAQ</span></a>
    <a class="tab" style="left:811px;width:126px"><span>Contact us</span></a>
    <a class="tab" style="left:944px;width:119px"><span>Login</span></a>
    <a class="tab" style="left:1070px;width:127px"><span>Register</span></a>
  </nav>
</header>

<main class="main">
  <h2 class="section-title">Latest Products</h2>
  <div class="pager-info">Showing 6 of 30</div>
  <div class="pager-btn" style="left:789px"><svg width="8" height="12"><path d="M6 1 1 6l5 5" fill="none" stroke="#999" stroke-width="1.5"/></svg></div>
  <div class="pager-btn" style="left:823px"><svg width="8" height="12"><path d="M2 1l5 5-5 5" fill="none" stroke="#999" stroke-width="1.5"/></svg></div>

  <article class="card" style="left:20px;top:63px">
    <div class="photo" role="img" aria-label="Coffee beans spilling from a metal scoop onto a sack" style="background:linear-gradient(135deg,#6b3a1e,#3a1d0c 60%,#8a6240)"></div>
    <div class="price">Price : 220 $</div>
    <div class="time-label"><svg width="22" height="22"><circle cx="11" cy="11" r="11" fill="#c8876a"/><path d="M11 5v6h5" stroke="#fff" stroke-width="2" fill="none"/></svg>Time Remaining</div>
    <div class="timer">15 : 23 : 45 &nbsp;Hrs</div>
  </article>
  <article class="card" style="left:441px;top:63px">
    <div class="photo" role="img" aria-label="Scoops resting in an open sack of roasted beans" style="background:radial-gradient(circle at 50% 60%,#6e3c1c,#2a1408 70%,#120804)"></div>
    <div class="price">Price : 220 $</div>
    <div class="time-label"><svg width="22" height="22"><circle cx="11" cy="11" r="11" fill="#c8876a"/><path d="M11 5v6h5" stroke="#fff" stroke-width="2" fill="none"/></svg>Time Remaining</div>
    <div class="timer">15 : 23 : 45 &nbsp;Hrs</div>
  </article>

  <article class="card" style="left:20px;top:245px">
    <div class="photo" role="img" aria-label="Latte art in a white cup with beans on the saucer" style="background:radial-gradient(circle at 45% 40%,#c08a5a,#e8e0d8 55%,#4a2a18)"></div>
    <div class="price">Price : 220 $</div>
    <div class="time-label"><svg width="22" height="22"><circle cx="11" cy="11" r="11" fill="#c8876a"/><path d="M11 5v6h5" stroke="#fff" stroke-width="2" fill="none"/></svg>Time Remaining</div>
    <div class="timer">15 : 23 : 45 &nbsp;Hrs</div>
  </article>
  <article class="card" style="left:441px;top:245px">
    <div class="photo" role="img" aria-label="Brown cup filled with beans on a bed of beans" style="background:radial-gradient(circle at 55% 45%,#8a4a24,#5a3018 50%,#3a1e0e)"></div>
    <div class="price">Price : 220 $</div>
    <div class="time-label"><svg width="22" height="22"><circle cx="11" cy="11" r="11" fill="#c8876a"/><path d="M11 5v6h5" stroke="#fff" stroke-width="2" fill="none"/></svg>Time Remaining</div>
    <div class="timer">15 : 23 : 45 &nbsp;Hrs</div>
  </article>

  <article class="card" style="left:20px;top:426px">
    <div class="photo" role="img" aria-label="Steaming cup of coffee with beans and spices on a dark table" style="background:linear-gradient(160deg,#5a2410,#2a0e06 55%,#8a6a40)"></div>
    <div class="price">Price : 220 $</div>
    <div class="time-label"><svg width="22" height="22"><circle cx="11" cy="11" r="11" fill="#c8876a"/><path d="M11 5v6h5" stroke="#fff" stroke-width="2" fill="none"/></svg>Time Remaining</div>
    <div class="timer">15 : 23 : 45 &nbsp;Hrs</div>
  </article>
  <article class="card" style="left:441px;top:426px">
    <div class="photo" role="img" aria-label="Mug of cappuccino beside beans, hazelnuts and cinnamon" style="background:linear-gradient(120deg,#f1e4cf,#a5643a 45%,#5a3018)"></div>
    <div class="price">Price : 220 $</div>
    <div class="time-label"><svg width="22" height="22"><circle cx="11" cy="11" r="11" fill="#c8876a"/><path d="M11 5v6h5" stroke="#fff" stroke-width="2" fill="none"/></svg>Time Remaining</div>
    <div class="timer">15 : 23 : 45 &nbsp;Hrs</div>
  </article>
</main>

<footer class="site-footer">
  <span class="copy">© CupTradeHub</span>
  <span class="rights">All Rights Reserved</span>
</footer>

<aside class="sidebar">
  <h2 class="side-title">Search Products</h2>
  <div class="field" style="left:14px;top:86px;width:299px;height:41px">Enter the keyword
    <svg class="abs" style="right:10px;top:9px" width="24" height="22"><circle cx="9" cy="9" r="6.5" fill="none" stroke="#999" stroke-width="2.5"/><path d="M14 13l7 6" stroke="#999" stroke-width="3.5" stroke-linecap="round"/></svg>
  </div>
  <div class="select" style="left:14px;top:141px;width:148px;height:40px">Select Location</div>
  <div class="select" style="left:166px;top:141px;width:148px;height:40px">Select category</div>
  <div class="select" style="left:14px;top:203px;width:299px;height:40px">Select the Brand / Comapany / Industry</div>

  <div class="range-label">Select the price range ($)</div>
  <div class="ticks">
    <span style="left:4px">0</span><span style="left:49px">50</span><span style="left:95px">100</span><span style="left:140px">150</span><span style="left:186px">200</span><span style="left:231px">250</span><span style="left:277px">300</span>
  </div>
  <svg class="abs" style="left:13px;top:317px" width="296" height="14"><g stroke="#888" stroke-width="1"><path d="M4 6v8M49 6v8M95 6v8M140 6v8M186 6v8M231 6v8M277 6v8"/></g></svg>
  <div class="track"><i></i></div>
  <svg class="handle" style="left:14px" width="16" height="22"><path d="M1 6 8 1l7 5v15H1z" fill="#d8d8d8" stroke="#999"/></svg>
  <svg class="handle" style="left:277px" width="16" height="22"><path d="M1 6 8 1l7 5v15H1z" fill="#d8d8d8" stroke="#999"/></svg>

  <div class="btn btn-primary">Search Product</div>
  <div class="btn btn-light">Clear Fields</div>

  <div class="ad-slot"><div class="size">260 X 150</div><div class="hint">Advertise Here</div></div>
</aside>

</body>
</html>
```